Mailing Flyer for Fruit Box Company

Need to design a postcard (2 sides) with both sides completed which will be mailed to companies.

The flyer needs to represent the following point in a graphical way.

1. Our team has sophisticated experience and knowledge in the produce industry that will undoubtedly leave you satisfied.
2. We’ve collaborated with many of our finest local growers that of which have been around for numerous generations such as, Copper Hollow Orchards (GIVE MORE LOCAL GROWER EXAMPLES).
3. We have insight on the finest grown fruits; including great judgement as to when they will taste their best.
4. Our company guarantees you get the most superior fruits at the peak of their seasons.
5. With our trustworthy team you can depend on us to satisfy all of your wants and needs.
6. Our farmers grow sustainable produce to help ensure that our future ecosystem is at its absolute best.
7. We have the type of fruits that will not only leave your tastebuds and heart fulfilled, but will cause you to want more after every order.
8. We’ve performed a wholesale business with the farmers in order to grant our customers the freshest fruits at their best valued price.
9. Now that you're able to order from any location in the United States say goodbye to standing in long lines at the grocery stores.
10. Our complementary policy allows our customers to try your first box free of charge.

A summary of the above could be written as:
Our Harvest Lantern team has decades of expertise in the produce industry, which we utilize to make insightful decisions on the produce we provide for our customers. We have collaborated with the multi-generational farms such as Copper Hollow Orchards to guarantee we supply fruits at the peak of their season. We are an environmentally conscious business, and buy sustainable produce from local growers. When you buy a box from The Harvest Lantern you can say goodbye to standing in long lines at the grocery store, enjoy fresh fruit at their best valued price, and receive the first box free of charge.

The point is to illustrate the above, not to have a lot of text since no one reads.
One side is for the mailing so it should have a space to put a sticker for the mailing address to send the mail to.

Size should be 8.5 width x 5.5 high (21.5cm width x 14cm hight)
We will also provide you with the logo of the company (see attached)

Target Market(s)

Offices in the San Francisco Bay Area

Colors

Designer to choose colors to be used in the design.

Requirements
Must have
• Nice photos of Fruits, Fruit boxes, Maybe a nice office meeting room with a nice fruit box on the table, maybe a picture of a beautiful farm. Something inspiring.
• Need to illustrate that products and boxes are delivered to companies.
• Need to give a feeling that this is an Exclusive Service, with the most highest quality fruits and services
• Need to have project in JPG and a format which support edit from our side, with possible layers or vectors.

```html
<!DOCTYPE html>
<html lang="en">
<head>
<meta charset="utf-8">
<title>The Harvest Lantern – Postcard</title>
<link href="https://fonts.googleapis.com/css2?family=Bebas+Neue&family=Lato:ital,wght@0,400;0,700;1,400&family=Roboto:wght@700&display=swap" rel="stylesheet">
<style>
  :root{
    --ink:#231f20;
    --band:#2a2120;
    --red:#e2231a;
    --rust:#c8401f;
    --orange:#f26522;
    --green:#2e9e48;
    --paper:#ffffff;
    --stage:#e9e9e9;
    --head:"Bebas Neue", "Oswald", sans-serif;
    --body:"Lato", "Helvetica Neue", sans-serif;
    --num:"Roboto", Arial, sans-serif;
  }
  *{box-sizing:border-box;margin:0;padding:0}
  html,body{width:902px;height:1200px;overflow:hidden;background:var(--stage)}
  .card{position:absolute;left:17px;width:868px;height:564px;background:var(--paper);overflow:hidden}
  .card--front{top:24px}
  .card--back{top:612px}
  .card svg.shapes{position:absolute;left:0;top:0}
  .abs{position:absolute}

  /* front */
  .bg-fruit{left:0;top:220px;width:480px;height:200px;border-radius:50%;
    background:radial-gradient(ellipse at 40% 50%,rgba(244,190,120,.45),rgba(250,225,200,.25) 55%,rgba(255,255,255,0) 75%)}
  .headline{left:42px;top:28px;font-family:var(--head);font-size:76px;line-height:1;color:var(--ink);letter-spacing:.5px}
  .subhead{left:42px;top:110px;font-family:var(--head);font-size:48px;line-height:1;color:var(--rust)}
  .tag{font-family:var(--body);font-weight:700;color:var(--green);border:2px solid var(--green);text-align:center;background:#fff}
  .tag--fresh{left:220px;top:182px;width:54px;height:26px;border-radius:14px 14px 6px 6px;font-size:10px;line-height:22px}
  .tag--superior{left:218px;top:276px;width:56px;height:30px;border-radius:6px;font-size:8px;line-height:11px;padding-top:3px;font-style:italic}
  .blurb{width:400px;font-family:var(--body);font-style:italic;font-size:13.5px;line-height:17px;color:var(--ink);text-align:center}
  .blurb--one{left:40px;top:222px}
  .blurb--two{left:40px;top:318px}
  .fruit-photo{left:540px;top:190px;width:320px;height:220px;border-radius:45%;
    background:radial-gradient(ellipse at 50% 55%,#f4a23a,#e5612c 40%,#8cb84a 70%,rgba(255,255,255,0) 78%)}
  .brand{left:606px;top:28px;width:144px;height:144px;border-radius:50%;border:3px solid var(--ink);background:#fff;
    display:flex;align-items:center;justify-content:center;text-align:center;font-family:var(--head);font-size:24px;line-height:1.05;color:var(--ink)}
  .call{left:62px;top:426px;font-family:var(--head);font-size:38px;color:var(--red)}
  .phone-big{left:110px;top:462px;font-family:var(--num);font-size:56px;color:#fff;letter-spacing:-.5px}
  .offer{left:560px;top:402px;width:232px;height:110px;border-radius:50%;
    background:radial-gradient(ellipse at 50% 20%,#f7b24a,#ee7a28 55%,#d9341d);text-align:center;font-family:var(--head);color:var(--ink)}
  .offer__line{font-size:17px;line-height:20px}
  .offer__line:first-child{margin-top:12px}
  .offer__pill{display:inline-block;margin-top:3px;padding:0 10px;border-radius:10px;background:var(--band);color:#fff;font-family:var(--body);font-size:11px;line-height:17px}
  .offer__free{font-size:25px;line-height:26px;color:#fff}

  /* back */
  .garden-photo{left:0;top:0;width:520px;height:275px;background:linear-gradient(135deg,#6f9a48,#a8c66a 45%,#c0523a 70%,#5c7f3a)}
  .people-photo{left:345px;top:270px;width:200px;height:200px;border-radius:50%;border:4px solid #fff;
    background:radial-gradient(circle at 45% 40%,#e7d4bf,#b7a08a 55%,#8a8f9a)}
  .brand--small{left:500px;top:18px;width:112px;height:112px;font-size:19px;border-width:2px}
  .stamp{left:714px;top:38px;width:112px;height:113px;border:1.5px solid #555}
  .addr-line{left:577px;width:261px;height:0;border-top:1px solid #777}
  .points{left:36px;top:290px;width:300px;list-style:none;font-family:var(--body);font-style:italic;font-size:12px;line-height:15.5px;color:var(--ink)}
  .points li{position:relative;padding-left:18px;margin-bottom:10px}
  .points li::before{content:"";position:absolute;left:0;top:4px;width:9px;height:9px;border-radius:50%;background:var(--orange)}
  .contact-title{left:42px;top:470px;font-family:var(--body);font-weight:700;font-size:16px;color:var(--orange)}
  .contact{left:42px;font-family:var(--body);color:#fff;display:flex;align-items:center;gap:8px}
  .contact--phone{top:494px;font-size:19px}
  .contact--mail{top:520px;font-size:13.5px}
  .follow{left:300px;top:476px;font-family:var(--body);font-size:13.5px;color:#fff;text-align:center}
  .follow__dots{display:flex;gap:3px;justify-content:center;margin-top:7px}
  .follow__dots span{width:19px;height:19px;border-radius:50%;background:var(--red)}
</style>
</head>
<body>

<section class="card card--front">
  <div class="abs bg-fruit" role="img" aria-label="Soft faded photo of assorted fresh fruit"></div>

  <svg class="shapes" width="868" height="564" viewBox="0 0 868 564">
    <circle cx="745" cy="300" r="272" fill="#fff"/>
    <path d="M630,54 A272,272 0 0 1 953,125" fill="none" stroke="var(--ink)" stroke-width="14"/>
    <path d="M630,54 A272,272 0 0 0 489,393" fill="none" stroke="var(--red)" stroke-width="9"/>
    <path d="M0,432 C150,388 330,392 500,415" fill="none" stroke="var(--red)" stroke-width="4"/>
    <path d="M0,445 C140,398 320,402 470,425 C560,440 650,472 868,468 L868,564 L0,564 Z" fill="var(--band)"/>
    <circle cx="478" cy="372" r="58" fill="var(--band)" stroke="#fff" stroke-width="4"/>
    <circle cx="478" cy="372" r="36" fill="none" stroke="var(--green)" stroke-width="3"/>
    <g transform="translate(80,498)" fill="none" stroke="var(--red)" stroke-width="3">
      <circle cx="0" cy="0" r="20"/>
      <path d="M-8,-10 q-4,3 -1,10 q4,9 12,12 q5,2 7,-2 l-4,-4 q-3,2 -5,0 q-4,-3 -6,-7 q-1,-3 2,-4 z" fill="var(--red)" stroke-width="1"/>
    </g>
  </svg>

  <h1 class="abs headline">WE SUPPLY FRUITS</h1>
  <h2 class="abs subhead">AT THE PEAK OF THEIR SEASON</h2>

  <div class="abs tag tag--fresh">FRESH</div>
  <p class="abs blurb blurb--one">We are an environmentally conscious business, and buy sustainable produce from local growers</p>
  <div class="abs tag tag--superior">SUPERIOR<br>FRUITS</div>
  <p class="abs blurb blurb--two">When you buy a box from The Harvest Lantern you can say goodbye to standing in long lines at the grocery store</p>

  <div class="abs fruit-photo" role="img" aria-label="Photo of a wicker basket overflowing with pineapple, apples, grapes, melon, bananas and citrus"></div>
  <div class="abs brand">The Harvest<br>Lantern</div>

  <div class="abs call">CALL US TODAY!</div>
  <div class="abs phone-big">123-456-7890</div>

  <div class="abs offer">
    <div class="offer__line">ENJOY FRESH FRUIT AT</div>
    <div class="offer__line">THEIR BEST VALUED PRICE</div>
    <div class="offer__pill">RECEIVE THE FIRST BOX</div>
    <div class="offer__free">FREE OF CHARGE</div>
  </div>
</section>

<section class="card card--back">
  <div class="abs garden-photo" role="img" aria-label="Photo of a farmer picking ripe tomatoes in a garden"></div>

  <svg class="shapes" width="868" height="564" viewBox="0 0 868 564">
    <path d="M520,0 L868,0 L868,564 L440,564 C520,450 560,300 520,0 Z" fill="#fff"/>
    <path d="M420,0 C500,60 530,180 505,275" fill="none" stroke="var(--band)" stroke-width="14"/>
    <path d="M0,275 L505,275 L520,420 L0,420 Z" fill="#fff"/>
    <path d="M0,400 C140,405 260,425 400,440 L400,452 C260,438 140,420 0,418 Z" fill="var(--orange)"/>
    <path d="M0,448 C150,432 300,442 470,452 C460,490 450,530 432,564 L0,564 Z" fill="var(--band)"/>
    <g transform="translate(52,506)" fill="none" stroke="var(--orange)" stroke-width="1.6">
      <circle r="8"/>
      <path d="M-3,-4 q-2,1 0,4 q2,4 5,5 q2,1 3,-1 l-2,-2 q-1,1 -2,0 q-2,-1 -2,-3 q0,-1 1,-2 z" fill="var(--orange)" stroke-width=".6"/>
    </g>
    <g transform="translate(44,525)" fill="none" stroke="var(--orange)" stroke-width="1.6">
      <rect width="14" height="10" fill="var(--orange)"/>
      <path d="M0,0 L7,6 L14,0" stroke="var(--band)" stroke-width="1.2"/>
    </g>
  </svg>

  <div class="abs people-photo" role="img" aria-label="Photo of colleagues enjoying a fruit box at an office table"></div>
  <div class="abs brand brand--small">The Harvest<br>Lantern</div>

  <div class="abs stamp"></div>
  <div class="abs addr-line" style="top:274px"></div>
  <div class="abs addr-line" style="top:325px"></div>
  <div class="abs addr-line" style="top:380px"></div>

  <ul class="abs points">
    <li>Our Harvest Lantern team has decades of expertise in the produce industry, which we utilize to make insightful decisions on the produce we provide for our customers.</li>
    <li>We have collaborated with the multi-generational farms such as Copper Hollow Orchards to guarantee</li>
  </ul>

  <div class="abs contact-title">CONTACT US TODAY!</div>
  <div class="abs contact contact--phone" style="left:68px">123-456-7890</div>
  <div class="abs contact contact--mail" style="left:68px">info@companyname.com</div>

  <div class="abs follow">Follow us on
    <div class="follow__dots"><span></span><span></span><span></span></div>
  </div>
</section>

</body>
</html>
```